Independent Financial Advisor Billboard Campaign - Granite Bridge Financial

I am a local, independent financial advisor. My company is Granite Bridge Financial, located in Charleston, WV. My main source of revenue comes from those nearing or entering retirement that need assistance with financial planning and investment management. Many are looking to rollover their employer retirement plan into an IRA account. I would like a billboard design campaign that focuses on this type of client. Please see our website www.granitebridgefinancial-example.com for more information.

```html
<!DOCTYPE html>
<html lang="en">
<head>
<meta charset="utf-8">
<title>Granite Bridge Financial – Billboard</title>
<link href="https://fonts.googleapis.com/css2?family=Outfit:wght@400;600&display=swap" rel="stylesheet">
<style>
  :root {
    --page: #d9dadb;
    --board-light: #ecebe8;
    --band-light: #f4f3f0;
    --navy: #17467f;
    --photo-blue: #2f62a0;
    --photo-blue-soft: #5a86b8;
    --white: #ffffff;
  }
  html, body {
    margin: 0;
    padding: 0;
    width: 1200px;
    height: 776px;
    overflow: hidden;
    background: var(--page);
  }
  .billboard {
    position: absolute;
    left: 20px;
    top: 93px;
    width: 1160px;
    height: 590px;
    background: var(--band-light);
    overflow: hidden;
    font-family: "Outfit", sans-serif;
  }
  .billboard-shapes {
    position: absolute;
    inset: 0;
  }
  .site-url {
    position: absolute;
    left: 133px;
    top: 28px;
    margin: 0;
    color: var(--white);
    font-size: 18px;
    font-weight: 400;
    letter-spacing: 2.5px;
  }
  .headline {
    position: absolute;
    left: 359px;
    top: 212px;
    margin: 0;
    color: var(--white);
    line-height: 1;
  }
  .headline-lead {
    display: block;
    font-size: 46px;
    font-weight: 400;
  }
  .headline-main {
    display: block;
    margin: 14px 0 0 29px;
    font-size: 72px;
    font-weight: 600;
  }
  .brand {
    position: absolute;
    left: 690px;
    top: 500px;
    display: flex;
    align-items: center;
    gap: 14px;
  }
  .brand-mark {
    width: 30px;
    height: 30px;
    background: var(--navy);
  }
  .brand-name {
    color: var(--navy);
    font-size: 32px;
    font-weight: 600;
  }
</style>
</head>
<body>
  <div class="billboard">
    <svg class="billboard-shapes" width="1160" height="590" viewBox="0 0 1160 590">
      <defs>
        <linearGradient id="couplePhoto" x1="0" y1="0" x2="1" y2="1">
          <stop offset="0" stop-color="#3e73ad"/>
          <stop offset="0.5" stop-color="var(--photo-blue-soft)"/>
          <stop offset="1" stop-color="var(--photo-blue)"/>
        </linearGradient>
        <linearGradient id="advisorPhoto" x1="0" y1="0" x2="0" y2="1">
          <stop offset="0" stop-color="#c99c82"/>
          <stop offset="0.35" stop-color="#e6e6e8"/>
          <stop offset="1" stop-color="#f2f2f3"/>
        </linearGradient>
      </defs>
      <rect class="left-strip" x="0" y="0" width="108" height="470" fill="var(--board-light)"/>
      <rect class="couple-photo" x="108" y="0" width="1042" height="470" fill="url(#couplePhoto)" role="img" aria-label="Blue-tinted photo of a smiling retired couple outdoors"/>
      <polygon class="accent-top" points="618,0 710,0 710,100" fill="var(--navy)"/>
      <polygon class="accent-main" points="52,59 462,538 0,538 0,470 52,470" fill="var(--navy)"/>
      <polygon class="accent-inner" points="112,243 270,430 112,430" fill="var(--board-light)"/>
      <rect class="advisor-photo" x="104" y="181" width="240" height="361" rx="60" fill="url(#advisorPhoto)" role="img" aria-label="Portrait of the advisor in a white polo shirt"/>
    </svg>
    <p class="site-url">www.granitebridgefinancial-example.com</p>
    <h1 class="headline">
      <span class="headline-lead">Plan your</span>
      <span class="headline-main">Financial Future !</span>
    </h1>
    <div class="brand">
      <span class="brand-mark"></span>
      <span class="brand-name">Granite Bridge Financial</span>
    </div>
  </div>
</body>
</html>
```